Events company needs professional workshop flyer design

We need a flyer design to advertise a workshop we are holding. The workshop is for professionals (Speech Pathologists, teachers, Psychologists).

I have attached a flyer with all the information in it. We need the flyer to look modern, and attract the attention of teachers to read it, to encourage them to attend a course to further their knowledge and skills.

It needs to list (as per flyer attached):
- The title of the workshop "Decoding Verbal Hurdles:Across Early Years and Teenage Life. Screening - Methods - Horizons
- Presented by Professor Maren Lisle-Tobacco (Speech & Language Therapist) & Professor Arlo Penwick (Developmental Psychologist)
- The 4 separate locations it is being held (with dates, and addresses)
- A section for intro of "expert speakers...etc"
- A section for topics to be covered
- A section for learning outcomes of the workshop
- Price
- Registration methods
- Who should attend the workshop
- Bio's of both speakers

It needs to be an A4 vertical brochure that is double sided.

```html
<!DOCTYPE html>
<html lang="en">
<head>
<meta charset="utf-8">
<title>Decoding Verbal Hurdles – Workshop Flyer</title>
<link href="https://fonts.googleapis.com/css2?family=Crimson+Text:ital,wght@0,400;0,600;0,700;1,400;1,600&family=Oswald:wght@600&display=swap" rel="stylesheet">
<style>
:root{
  --bg:#d9d9d7;
  --paper:#ffffff;
  --cream:#f5f2df;
  --olive:#a9b72c;
  --olive-soft:#e3e8b4;
  --maroon:#8a1c1c;
  --ink:#3a2f2b;
  --grey:#6d6a66;
  --blue:#5d82c6;
}
*{margin:0;padding:0;box-sizing:border-box}
html,body{width:1200px;height:900px;overflow:hidden;background:var(--bg)}
body{font-family:"Crimson Text",Georgia,serif;color:var(--ink);position:relative}
.page{position:absolute;top:26px;width:547px;height:818px;background:var(--paper);box-shadow:0 2px 10px rgba(0,0,0,.25);overflow:hidden}
.page--front{left:45px}
.page--back{left:618px}
.abs{position:absolute}

/* front header */
.title-block{left:30px;top:20px;width:360px;text-align:center}
.title-block h1{font-size:22px;line-height:1.1;font-weight:700;color:var(--ink)}
.title-block .sub{font-size:13px;font-weight:700;margin-top:3px}
.title-block .presenters{font-size:13px;line-height:1.2;margin-top:6px;color:var(--grey)}
.title-block .presenters em{font-size:11px}
.bubble-line{left:12px;top:14px}
.price-tag{left:398px;top:44px;width:126px;height:118px;background:var(--blue);border-radius:6px;color:#fff;text-align:center;padding-top:4px}
.brand{display:flex;align-items:center;gap:5px;justify-content:center;background:#fff;margin:0 6px;padding:3px 0;font-size:12px;font-weight:700;color:var(--blue)}
.brand i{width:9px;height:9px;background:var(--olive);display:inline-block}
.price-tag .big{font-size:19px;font-weight:700;margin-top:2px}
.price-tag .small{font-size:9.5px;line-height:1.1}
.price-tag .year{font-family:"Oswald",sans-serif;font-size:30px;line-height:1;text-align:right;padding-right:8px}

/* venues */
.venues{left:0;top:172px;width:547px;display:grid;grid-template-columns:repeat(4,1fr)}
.venue{border-right:2px solid #fff}
.venue:last-child{border-right:0}
.venue .when{background:var(--olive);color:#fff;padding:5px 8px;height:48px}
.venue .city{font-size:15px;font-weight:700;line-height:1}
.venue .date{font-size:14px;font-weight:700;line-height:1.05}
.venue .days{font-size:9px}
.venue .where{background:var(--olive-soft);padding:6px 8px;height:42px;font-size:11px;line-height:1.05}
.venue .where span{display:block;font-size:9px}

.intro{left:36px;top:266px;width:480px}
.intro .lead{font-size:13.5px;font-weight:700;line-height:1.15}
.intro .lead em{font-weight:700}
.intro p.body{font-size:11px;line-height:1.18;margin-top:7px;color:var(--grey)}

.tab{background:var(--maroon);color:#fff;font-size:12.5px;font-weight:600;padding:3px 14px;border-radius:3px 3px 0 0;position:absolute}
.tab::after{content:"";position:absolute;left:14px;bottom:-7px;border:7px solid transparent;border-top-color:var(--maroon);border-bottom:0}
.list-box{position:absolute;left:12px;width:523px;background:var(--cream);padding:9px 16px 7px 38px}
.list-box ul{list-style:none}
.list-box li{font-size:11px;line-height:1.18;color:var(--ink);position:relative}
.list-box li::before{content:"";position:absolute;left:-12px;top:5px;width:4px;height:4px;background:var(--maroon);border-radius:50%}
.topics-tab{left:30px;top:398px}
.topics{top:420px}
.outcomes-tab{left:30px;top:566px}
.outcomes{top:588px}
.band-bottom{left:0;bottom:0;width:547px;height:58px;background:var(--olive)}

/* back */
.about-tab{left:15px;top:30px;font-size:16px;padding:4px 46px 4px 50px;font-weight:700;letter-spacing:.5px}
.bio{left:15px;width:517px;display:flex;gap:12px}
.bio .photo{flex:0 0 100px;height:100px}
.bio h3{font-size:13px;font-style:italic;font-weight:700;line-height:1.1}
.bio p{font-size:10.8px;line-height:1.2;color:var(--ink);margin-top:3px}
.bio-1{top:84px}
.bio-1 .photo{background:linear-gradient(135deg,#5a5550,#2f2b28)}
.bio-2{top:222px}
.bio-2 .photo{height:112px;background:linear-gradient(135deg,#cfcac2,#8e8880)}
.bio-text{border-top:1px solid #ddd;padding-top:4px}
.bio-text .head{background:var(--cream);padding:2px 4px}
.rule{left:40px;width:467px;height:1px;background:#cfc9c0}
.attend{left:0;top:370px;width:547px;text-align:center}
.attend .q{font-size:18px;font-style:italic;color:var(--grey)}
.attend .who{font-size:17px;font-weight:600;color:var(--maroon);line-height:1.2;margin-top:2px}
.col-head{font-family:"Oswald",sans-serif;font-size:24px;color:var(--maroon);line-height:1}
.cost-head{left:48px;top:492px}
.reg-head{left:263px;top:492px}
.head-rule{left:15px;top:522px;width:517px;height:2px;background:var(--maroon)}
.cost-box{left:15px;top:526px;width:195px;height:118px;background:var(--cream);text-align:center;padding-top:6px}
.cost-box .big{font-size:19px;font-weight:600}
.cost-box p{font-size:12px;line-height:1.15;color:var(--maroon)}
.cost-box small{display:block;font-size:8.5px;font-style:italic;color:var(--ink);margin-top:3px}
.register{left:220px;top:530px;width:312px;text-align:center;font-size:9px;color:var(--grey);line-height:1.35}
.register strong{display:block;font-size:12.5px;color:var(--ink);margin:2px 0}
.policy{left:15px;top:654px;width:360px;font-size:8.6px;line-height:1.2;color:var(--ink)}
.policy p+p{margin-top:5px}
.back-brand{left:388px;top:690px;width:144px;border:1px solid #ddd;padding:4px}
.back-brand .brand{margin:0}
</style>
</head>
<body>

<section class="page page--front" aria-label="Flyer front">
  <svg class="abs bubble-line" width="380" height="160" viewBox="0 0 380 160" aria-hidden="true">
    <path d="M2 14 L2 150 L376 150" fill="none" stroke="#e2ddd0" stroke-width="1.5"/>
    <path d="M2 14 L22 2 L22 14 Z" fill="#fff" stroke="#e2ddd0"/>
  </svg>
  <div class="abs title-block">
    <h1>Decoding Verbal Hurdles:<br>Across Early Years and Teenage Life</h1>
    <div class="sub">Screening - Methods - Horizons</div>
    <div class="presenters"><em>Presented by</em><br>Professor Maren Lisle-Tobacco (Speech &amp; Language Therapist)<br>&amp;<br>Professor Arlo Penwick (Psychologist).</div>
  </div>
  <div class="abs price-tag">
    <div class="brand"><i></i>WORDWISE</div>
    <div class="big">2 days: $495</div>
    <div class="small">(Earlybird)<br>Add an additional $88<br>if registering within 3<br>weeks of workshop</div>
    <div class="year">2015</div>
  </div>

  <div class="abs venues">
    <div class="venue"><div class="when"><div class="city">Brisbane</div><div class="date">9th-10th February</div><div class="days">(Monday-Tuesday)</div></div><div class="where">Ridgeway Social Club<span>41 Tallow Rd, Kelvin Hill</span></div></div>
    <div class="venue"><div class="when"><div class="city">Sydney</div><div class="date">12th-13th February</div><div class="days">(Thursday-Friday)</div></div><div class="where">Westbrook Lions Hall<span>Cnr Alder St and Quarry Rd, Westbrook</span></div></div>
    <div class="venue"><div class="when"><div class="city">Melbourne</div><div class="date">5th-6th March</div><div class="days">(Thursday-Friday)</div></div><div class="where">Harbourline Hotel<span>22-28 Fenwick St, Melbourne</span></div></div>
    <div class="venue"><div class="when"><div class="city">Perth</div><div class="date">17th -18th March</div><div class="days">(Tuesday-Wednesday)</div></div><div class="where">Coralgate Inn<span>9 Marlow Ave, Eastshore</span></div></div>
  </div>

  <div class="abs intro">
    <p class="lead">Expert International Speakers, Speech Language Therapist <em>Maren Lisle-Tobacco</em> and Developmental Psychologist <em>Dr Arlo Penwick</em> are coming to Australia in February and March 2015.</p>
    <p class="body">Limited places are available for their two day event focusing on language difficulties in children. Professors Lisle-Tobacco and Penwick are world leading scientists who bring years of expertise and their specific interest in both clinical practice and research. They will share their knowledge with you and use videos, case studies and discussions to develop your practical skills and strategies to use in the clinical setting and classroom.</p>
  </div>

  <div class="tab topics-tab">Topics to be covered include:</div>
  <div class="list-box topics">
    <ul>
      <li>Language Difficulties - terminology, diagnosis, assessment &amp; intervention strategies</li>
      <li>Autism Spectrum Disorders (ASD) and language difficulties—Links, overlaps and differences</li>
      <li>Developmental trajectories—How language difficulties change from childhood to adolescence</li>
      <li>The IQ problem: Nonverbal skills in children with Language difficulties</li>
      <li>Social, emotional and behavioural difficulties: Problems at different stages of development for children with language difficulties.</li>
      <li>Tablets/Apps/New media and children with Language difficulties— what do they mean for these children.</li>
    </ul>
  </div>

  <div class="tab outcomes-tab">Learning outcomes of the workshop:</div>
  <div class="list-box outcomes">
    <ul>
      <li>To build a developmental framework for assessment and intervention of language difficulties from early childhood to adolescence.</li>
      <li>To know what are the red flags that need to be targets of intervention</li>
      <li>To determine the key principles that identify and differentiate Language difficulties vs ASD in early childhood, middle childhood and adolescence</li>
      <li>To predict who is most at risk of social, emotional and behavioural difficulties and learn what to target in intervention, with whom, and why</li>
      <li>To understand the impact of the digital world for language, literacy and educational attainment</li>
      <li>To know the benefits of professional therapy, and how you can shift the educational outcomes of young people with language difficulties.</li>
    </ul>
  </div>
  <div class="abs band-bottom"></div>
</section>

<section class="page page--back" aria-label="Flyer back">
  <div class="tab about-tab">ABOUT</div>

  <div class="abs bio bio-1">
    <div class="photo" role="img" aria-label="Portrait photo of Professor Maren Lisle-Tobacco"></div>
    <div class="bio-text">
      <h3 class="head">Professor Maren Lisle-Tobacco</h3>
      <p>Maren is Professor of Child Language and Learning at the University of Northmere, UK. She is the director of a nationwide longitudinal study on specific language impairment (SLI) that has been following individuals from 7 years of age to adult life. Maren has an interest in the interface between clinical practice and research. She is founder member of the SPEAK campaign to raise awareness of SLI (www.speakcampaign.org/videos), was editor of the Journal of Speech and Language Studies and was involved in the development of national clinical guidelines for language disorders in children.</p>
    </div>
  </div>

  <div class="abs bio bio-2">
    <div class="photo" role="img" aria-label="Portrait photo of Professor Arlo Penwick"></div>
    <div class="bio-text">
      <h3 class="head">Professor Arlo Penwick</h3>
      <p>Arlo Penwick is Professor of Psychology at the University of Glenhaven, UK. He has previously held a Chair at Westland University and was Director of the WU Child Growth Centre. He has a longestablished interest in language difficulties and child development. He has written a large number of journal articles and books for academics and practitioners, and is editor of the journal Early Words Review. For the past ten years he has been co-directing the longitudinal study of SLI with Maren Lisle-Tobacco.</p>
    </div>
  </div>

  <div class="abs rule" style="top:360px"></div>
  <div class="abs attend">
    <div class="q">Who should attend?</div>
    <div class="who">For Teachers, Speech Pathologists, Psychologists and<br>those interested in learning more about<br>children with Language Learning difficulties</div>
  </div>

  <div class="abs col-head cost-head">COST</div>
  <div class="abs col-head reg-head">TO REGISTER</div>
  <div class="abs head-rule"></div>
  <div class="abs cost-box">
    <div class="big">2 days: $495</div>
    <p>(Earlybird)<br>Add an additional $88 if registering within 3 weeks of workshop.</p>
    <small>(incl G.S.T, workshop materials, morning and afternoon tea, lunch)</small>
  </div>
  <div class="abs register">
    online at
    <strong>http://www.wordwisestudio.example/events/</strong>
    or Call Nora Vellan on
    <strong>02 5550 1847</strong>
    or email
    <strong>events@wordwisestudio.example</strong>
    for invoicing for your school or workplace
  </div>

  <div class="abs policy">
    <p><strong>Cancellation Policy</strong> - In the event that a participant cancels, The registration fee minus a 10% processing fee ($49.50) will be refunded until Thursday 22nd January 2015. After this date, there will be no refund.</p>
    <p>If the hosts cancel (Wordwise Speech Studio), or defers the event, 100% of the registration fee will be refunded if the registrant cannot attend on the revised dates, however the hosts bear no responsibility for any costs incurred (such as flights, accommodation, travel expenses) or loss of income.</p>
  </div>
  <div class="abs back-brand"><div class="brand"><i></i>WORDWISE</div></div>
  <div class="abs band-bottom" style="height:34px"></div>
</section>

</body>
</html>
```